MD Business Card

I want to create a simple business card.
I am a consultant. I design and develop furniture, lighting and accessories for hospitality and retail brands.
I want the card to be simple and clean. Not too much of a logo - but it needs the basic information shown on the attached file.
Also - I have shown some fonts that I like on the attached file.
The card can be square or rectangle. It should be double sided.
I prefer 1-2 colors (not too colorful - but using color an an accent) Even if using color on the edges as an accent.

My snapquilt link shows some other graphics styles that I like. I like clean and simple.
http://www.snapquilt.com/marendowsett/business-cards/

Reason: I needed a few more days to see some of the options evolve.

Hospitality

```html
<!DOCTYPE html>
<html lang="en">
<head>
<meta charset="utf-8">
<title>MD Business Card</title>
<link href="https://fonts.googleapis.com/css2?family=Oswald:wght@300;400&display=swap" rel="stylesheet">
<style>
  :root {
    --backdrop: #ecebe8;
    --card-white: #f4f4f2;
    --card-mint: #dfe5df;
    --ink: #5a5c5e;
    --ink-soft: #8a8c8e;
    --rule: #d3d4d2;
    --coral: #e4675f;
  }
  * { margin: 0; padding: 0; box-sizing: border-box; }
  html, body {
    width: 1200px; height: 900px; overflow: hidden;
    background: var(--backdrop);
    font-family: "Oswald", sans-serif;
  }
  .canvas {
    width: 1200px; height: 900px;
    display: flex; flex-direction: column;
    align-items: center; justify-content: center; gap: 48px;
  }
  .card {
    position: relative;
    width: 640px; height: 366px;
    background: var(--card-white);
    box-shadow: 0 6px 18px rgba(0,0,0,.12);
    overflow: hidden;
  }
  /* back side: details */
  .card-details .rule-horizontal {
    position: absolute; left: 0; right: 0; top: 178px;
    border-top: 1px solid var(--rule);
  }
  .card-details .rule-vertical {
    position: absolute; left: 348px; top: 100px; height: 160px;
    border-left: 1px solid var(--rule);
  }
  .identity {
    position: absolute; right: 312px; top: 124px; text-align: right;
  }
  .identity-name {
    font-weight: 300; font-size: 36px; letter-spacing: 1.5px;
    color: var(--ink); text-transform: uppercase; line-height: 1;
  }
  .identity-role {
    margin-top: 16px;
    font-weight: 300; font-size: 16px; letter-spacing: 3px;
    color: var(--ink-soft); text-transform: uppercase;
  }
  .contact {
    position: absolute; left: 372px; top: 130px;
  }
  .contact-phone {
    font-weight: 300; font-size: 24px; letter-spacing: 2px;
    color: var(--ink); line-height: 1;
  }
  .contact-email {
    margin-top: 24px;
    font-weight: 300; font-size: 13px; letter-spacing: 2px;
    color: var(--ink-soft); text-transform: uppercase;
  }
  .accent { color: var(--coral); font-weight: 400; }
  /* front side: monogram */
  .card-front .split { position: absolute; inset: 0; }
  .monogram {
    position: absolute; left: 50%; top: 50%;
    transform: translate(-50%, -50%);
    font-weight: 400; font-size: 64px; letter-spacing: 4px;
    color: var(--coral); line-height: 1;
  }
</style>
</head>
<body>
<main class="canvas">
  <section class="card card-details" aria-label="Card back">
    <div class="rule-horizontal"></div>
    <div class="rule-vertical"></div>
    <div class="identity">
      <p class="identity-name">Maren Dowsett</p>
      <p class="identity-role">Hospitality <span class="accent">&amp;</span> Home</p>
    </div>
    <div class="contact">
      <p class="contact-phone">917.555.0148</p>
      <p class="contact-email">maren<span class="accent">@</span>marendowsett.com</p>
    </div>
  </section>

  <section class="card card-front" aria-label="Card front">
    <svg class="split" width="640" height="366" viewBox="0 0 640 366" aria-hidden="true">
      <rect width="640" height="366" fill="var(--card-white)"/>
      <polygon points="0,0 640,0 640,40 0,366" fill="var(--card-mint)"/>
    </svg>
    <p class="monogram">MD</p>
  </section>
</main>
</body>
</html>
```